Brochure for software platform

We need a clean and professional brochure (max 4 pages) for one of our products called "Jurnex.io", see https://jurnex-example.io/en. The product is a software platform to manage the application and selection process for grants, awards or similar challenges. Our company is called Larkmont Systems AG and we are based in Switzerland. The brochure should be in English but might be translated into German. The design should be based on the information provided on the website and in the presentation available on google drive (with logo,...). See
https://files.example-share.net/folders/8KpQ2vTz7LmW3xRd?share=link
Additional screenshots for mockups can be provided once closer to the final design. Design should be clean and professional.

Target Market(s)

Foundations, Investors, Accelerators, Award organisers

Font styles to use
Other font styles liked:
• Opens Sans Light

Colors
0492cd
34a6d7
85cae6
0255a3
3377b5

Requirements
Must have
• Use white (or bright) background. And the blue logo color for font titles. At least one mockup with a screenshot of the platform (see website). No must of customer logos but if it fits we can provide some (see as on website).

```html
<!DOCTYPE html>
<html lang="en">
<head>
<meta charset="utf-8">
<title>Jurnex brochure</title>
<link rel="stylesheet" href="https://fonts.googleapis.com/css2?family=Open+Sans:wght@300;400;600&display=swap">
<style>
:root{
  --backdrop:#bdbec1;
  --panel-blue:#6aaae0;
  --band-blue:#6ba9df;
  --title-blue:#3b8fd3;
  --deep-blue:#2a79c4;
  --text-grey:#6d6f73;
  --light-grey:#f4f5f7;
  --white:#ffffff;
}
*{box-sizing:border-box;margin:0;padding:0}
html,body{width:961px;height:1200px;overflow:hidden;background:var(--backdrop)}
body{font-family:"Open Sans",Arial,sans-serif;font-weight:300;color:var(--text-grey)}
.canvas{position:relative;width:961px;height:1200px}
.spread{position:absolute;left:48px;width:853px;background:var(--white);overflow:hidden}
.spread--outer{top:31px;height:550px}
.spread--inner{top:614px;height:551px}
.abs{position:absolute}
svg{display:block}

/* outer spread */
.back-cover{left:0;top:0;width:427px;height:550px;background:var(--panel-blue);color:var(--white)}
.back-cover h2{position:absolute;left:36px;top:47px;font-weight:300;font-size:17px;line-height:20px}
.service{position:absolute;top:101px;width:100px}
.service .label{margin-top:8px;font-size:9px;font-weight:400}
.service p{margin-top:10px;font-size:7.6px;line-height:10px;font-weight:400}
.wordmark{font-family:"Open Sans",Arial,sans-serif;font-weight:600;display:flex;align-items:center;gap:6px}
.wordmark .dot{width:.55em;height:.55em;border-radius:50%;background:currentColor}
.back-cover .wordmark{position:absolute;left:223px;top:366px;font-size:25px;color:var(--white)}
.contact{position:absolute;left:223px;top:412px;font-size:9px;line-height:11px;font-weight:400}
.contact p+p{margin-top:10px}

.cover-photo{left:427px;top:0;width:426px;height:306px;background:linear-gradient(160deg,#5b4a45 0%,#3a3d49 55%,#23242c 100%)}
.cover-white{left:427px;top:306px;width:426px;height:176px;background:#f3f4f6}
.cover-band{left:427px;top:482px;width:426px;height:68px;background:var(--band-blue)}
.cover-band p{text-align:center;color:var(--white);font-size:11px;letter-spacing:2px;font-weight:400;margin-top:31px}
.cover{left:427px;top:0;width:426px;height:550px}
.cover .wordmark{position:absolute;left:0;width:426px;justify-content:center;top:397px;font-size:30px;color:var(--title-blue)}
.cover .tagline{position:absolute;left:0;width:426px;top:440px;text-align:center;font-size:16px;color:#7c7e83}

/* inner spread */
.section-title{color:var(--title-blue);font-weight:300;font-size:17px}
.summary{left:27px;top:42px;width:230px}
.summary p{margin-top:8px;font-size:9px;line-height:11px}
.bullets{list-style:none;margin-top:8px;font-size:9px;line-height:11px}
.bullets li{display:flex;align-items:center;gap:5px}
.bullets li::before{content:"";width:5px;height:5px;border-radius:50%;background:var(--title-blue)}
.value-band{left:0;top:169px;width:470px;height:177px;background:linear-gradient(90deg,var(--light-grey),#fbfbfc)}
.added{left:29px;top:200px}
.added p{margin-top:4px;font-size:9px}
.benefit{position:absolute;top:242px;width:96px;text-align:center;font-size:8.8px;line-height:11px}
.benefit svg{margin:0 auto 7px}
.workflow-title{left:0;width:420px;top:362px;text-align:center}
.step{position:absolute;top:423px;width:84px}
.step h4{color:var(--title-blue);font-weight:400;font-size:9px}
.step p{margin-top:9px;font-size:8.3px;line-height:11px}

.overview-head{left:0;top:0;width:853px;height:57px}
.overview-head h2{position:absolute;left:465px;top:21px;color:var(--white);font-weight:300;font-size:18px}
.feature{position:absolute;left:492px;width:140px;font-size:7.8px;line-height:10px}
.feature h4{color:var(--deep-blue);font-weight:400;font-size:8px}
.feature svg{position:absolute;left:-26px;top:0}
.inner-wordmark{left:695px;top:274px;font-size:23px;color:var(--title-blue)}
.bottom-bar{left:0;top:541px;width:853px;height:10px;background:var(--band-blue)}
</style>
</head>
<body>
<div class="canvas">

  <section class="spread spread--outer">
    <div class="abs back-cover">
      <h2>Premium implementation services<br>and secure infrastructure</h2>

      <div class="service" style="left:36px">
        <svg width="28" height="26" viewBox="0 0 28 26" fill="none" stroke="#fff" stroke-width="1.2"><rect x="1" y="1" width="18" height="12" rx="1"/><path d="M5 13v4l4-4"/><rect x="9" y="9" width="18" height="11" rx="1" fill="#6aaae0"/><path d="M23 20v4l-4-4M12 13h12M12 16h9"/></svg>
        <div class="label">Dedicated support</div>
        <p>Dedicated service contracts for tailored and personal customer support.</p>
      </div>
      <div class="service" style="left:153px">
        <svg width="20" height="26" viewBox="0 0 20 26" fill="none" stroke="#fff" stroke-width="1.2"><path d="M4 11V7a6 6 0 0 1 12 0v4"/><rect x="1" y="11" width="18" height="14" rx="2"/><text x="10" y="21" fill="#fff" stroke="none" font-size="6" text-anchor="middle" font-family="Open Sans,sans-serif" font-weight="600">SSL</text></svg>
        <div class="label">Secure hosting</div>
        <p>Hosted in Swiss ISO and FINMA certified data center. Encrypted transmission.</p>
      </div>
      <div class="service" style="left:270px">
        <svg width="26" height="26" viewBox="0 0 26 26" fill="none" stroke="#fff" stroke-width="1.2"><circle cx="17" cy="8" r="5"/><circle cx="17" cy="8" r="2"/><circle cx="8" cy="18" r="5"/><circle cx="8" cy="18" r="2"/></svg>
        <div class="label">Reliable infrastructure</div>
        <p>Guaranteed infrastructure uptime of 99.9 % with scheduled maintenance.</p>
      </div>

      <div class="wordmark"><span class="dot"></span>Jurnex</div>
      <div class="contact">
        <p>A brand of Larkmont Systems AG<br>Lindenhofweg 12<br>8001 Zürich, Switzerland</p>
        <p>Email contact<br>mail@larkmont-example.ch</p>
        <p style="margin-top:14px">www.jurnex-example.io</p>
      </div>
    </div>

    <div class="abs cover-photo" role="img" aria-label="Photo of a speaker on stage at an accelerator event, audience in the foreground"></div>
    <div class="abs cover-white"></div>
    <div class="abs cover-band"><p>www.jurnex-example.io</p></div>

    <svg class="abs" style="left:518px;top:154px" width="236" height="240" viewBox="0 0 236 240">
      <defs><linearGradient id="standA" x1="0" y1="0" x2="0" y2="1"><stop offset="0" stop-color="#cfd1d4"/><stop offset="1" stop-color="#f3f4f6"/></linearGradient></defs>
      <path d="M97 162h42l6 44H91z" fill="url(#standA)"/>
      <ellipse cx="118" cy="210" rx="44" ry="6" fill="#e4e5e8"/>
      <rect x="1" y="0" width="234" height="162" rx="4" fill="#1b1c20"/>
      <rect x="9" y="8" width="218" height="144" fill="#ffffff" role="img" aria-label="Screenshot of the applications list in the platform"/>
      <rect x="9" y="8" width="45" height="144" fill="#2f3035"/>
      <rect x="54" y="8" width="173" height="8" fill="#eef0f3"/>
      <g fill="#e6e8ec"><rect x="62" y="66" width="158" height="3"/><rect x="62" y="75" width="158" height="3"/><rect x="62" y="84" width="158" height="3"/><rect x="62" y="93" width="158" height="3"/><rect x="62" y="102" width="158" height="3"/><rect x="62" y="111" width="158" height="3"/></g>
      <g fill="#6aaae0"><rect x="210" y="74" width="8" height="4"/><rect x="210" y="83" width="8" height="4"/><rect x="210" y="92" width="8" height="4"/><rect x="210" y="101" width="8" height="4"/><rect x="210" y="110" width="8" height="4"/></g>
    </svg>

    <div class="abs cover">
      <div class="wordmark"><span class="dot"></span>Jurnex</div>
      <p class="tagline">Smart Application Management</p>
    </div>
  </section>

  <section class="spread spread--inner">
    <svg class="abs overview-head" width="853" height="57" viewBox="0 0 853 57">
      <polygon points="287,0 853,0 853,57 368,57 342,30" fill="#6ba9df"/>
      <polygon points="281,0 299,0 350,47 340,47" fill="#2f7fc8"/>
    </svg>
    <div class="abs overview-head" style="pointer-events:none"><h2>Product overview</h2></div>

    <div class="abs value-band"></div>

    <div class="abs summary">
      <h2 class="section-title">Summary</h2>
      <p>Jurnex is a fully customized platform to efficiently manage the application, revision and selection process for grants, investments and awards.</p>
      <ul class="bullets">
        <li>Intuitive and branded user interface</li>
        <li>Customized and multi-step selection process</li>
        <li>Premium support and secure infrastructure</li>
      </ul>
    </div>

    <svg class="abs" style="left:232px;top:44px" width="190" height="112" viewBox="0 0 190 112">
      <rect x="20" y="0" width="150" height="104" rx="4" fill="#1b1c20"/>
      <rect x="25" y="5" width="140" height="95" fill="#fff" role="img" aria-label="Screenshot of the platform dashboard"/>
      <rect x="25" y="5" width="30" height="95" fill="#2f3035"/>
      <g fill="#e6e8ec"><rect x="60" y="40" width="100" height="2"/><rect x="60" y="47" width="100" height="2"/><rect x="60" y="54" width="100" height="2"/><rect x="60" y="61" width="100" height="2"/><rect x="60" y="68" width="100" height="2"/></g>
      <rect x="127" y="21" width="7" height="3" fill="#6aaae0"/>
      <path d="M0 104h190l-6 6H6z" fill="#b9bbbf"/>
    </svg>

    <div class="abs added">
      <h2 class="section-title">Added value</h2>
      <p>Smooth user experience and improved efficiency</p>
    </div>
    <div class="benefit" style="left:30px">
      <svg width="30" height="28" viewBox="0 0 30 28" fill="none" stroke="#3b8fd3" stroke-width="1.4"><circle cx="13" cy="13" r="12"/><path d="M16 9c-1-2-6-2-6 1s6 2 6 5-5 3-6 1M13 6v14"/><path d="M25 18v8M22 23l3 3 3-3" stroke-width="1.8"/></svg>
      Simplifies the application and selection process
    </div>
    <div class="benefit" style="left:147px">
      <svg width="30" height="28" viewBox="0 0 30 28" fill="none" stroke="#3b8fd3" stroke-width="1.4"><path d="M5 1h11l6 6v19H5z"/><path d="M16 1v6h6"/><circle cx="20" cy="21" r="5" fill="#fff"/><path d="M18 19l4 4M22 19l-4 4"/></svg>
      Eliminates the need of email and spreadsheets
    </div>
    <div class="benefit" style="left:272px">
      <svg width="32" height="30" viewBox="0 0 32 30" fill="none" stroke="#3b8fd3" stroke-width="1.4"><circle cx="13" cy="8" r="6"/><path d="M2 27c0-7 5-11 11-11 3 0 5 1 7 2"/><circle cx="25" cy="23" r="4"/><circle cx="25" cy="23" r="1.5"/></svg>
      Connects your brand with a positive user experience
    </div>

    <h2 class="abs section-title workflow-title">Clean and customized workflow</h2>
    <svg class="abs" style="left:29px;top:401px" width="410" height="16" viewBox="0 0 410 16">
      <line x1="0" y1="8" x2="410" y2="8" stroke="#3b8fd3" stroke-width="1"/>
      <g fill="#fff" stroke="#3b8fd3" stroke-width="1.2"><circle cx="15" cy="8" r="6"/><circle cx="107" cy="8" r="6"/><circle cx="199" cy="8" r="6"/><circle cx="290" cy="8" r="6"/></g>
    </svg>
    <div class="step" style="left:38px"><h4>Application</h4><p>Applicants submit their data through a dedicated and custom branded web portal.</p></div>
    <div class="step" style="left:130px"><h4>Revision</h4><p>Judges review applications on the portal through a tailored and multi-step process</p></div>
    <div class="step" style="left:222px"><h4>Selection</h4><p>Applications are selected based on evaluation scores and qualitative feedback</p></div>
    <div class="step" style="left:313px"><h4>Messaging</h4><p>The integrated messaging and feedback tools allow direct engagement.</p></div>

    <div class="feature" style="top:83px">
      <svg width="14" height="18" viewBox="0 0 14 18" fill="none" stroke="#3b8fd3" stroke-width="1.2"><path d="M1 1h8l4 4v12H1z"/><path d="M4 8h6M4 11h6M4 14h6"/></svg>
      <h4>Structured application process</h4>
      Application data is collected through web forms with dedicated field types, display logic and input validation.
    </div>
    <div class="feature" style="top:147px">
      <svg width="22" height="18" viewBox="0 0 22 18" fill="none" stroke="#3b8fd3" stroke-width="1.2" style="left:-32px"><rect x="8" y="1" width="6" height="4"/><rect x="1" y="13" width="5" height="4"/><rect x="8.5" y="13" width="5" height="4"/><rect x="16" y="13" width="5" height="4"/><path d="M11 5v4M3.5 13V9h15v4M11 9v4"/></svg>
      <h4>Tailored selection workflow</h4>
      The selection process can include multiple rounds, assessment and jury types.
    </div>
    <div class="feature" style="top:206px">
      <svg width="16" height="18" viewBox="0 0 16 18" fill="none" stroke="#3b8fd3" stroke-width="1.2"><rect x="1" y="1" width="14" height="16"/><path d="M4 5h8M4 8h8M4 11h5M4 14h8"/></svg>
      <h4>Multiple evaluation types</h4>
      Evaluation forms can include weighted point scores, yes/ no ratings, color scores or comments.
    </div>
    <div class="feature" style="top:263px">
      <svg width="18" height="20" viewBox="0 0 18 20" fill="none" stroke="#3b8fd3" stroke-width="1.2"><circle cx="9" cy="11" r="8"/><path d="M9 11l4-4M7 1h4"/></svg>
      <h4>Live analytics and portfolio<br>management</h4>
      Key application and performance data is visualized on interactive dashboards. Applications can be monitored beyond selection through integration with the portfolio management module.
    </div>

    <svg class="abs" style="left:648px;top:79px" width="184" height="166" viewBox="0 0 184 166">
      <defs><linearGradient id="standB" x1="0" y1="0" x2="0" y2="1"><stop offset="0" stop-color="#cfd1d4"/><stop offset="1" stop-color="#fafafa"/></linearGradient></defs>
      <path d="M76 125h32l5 34H71z" fill="url(#standB)"/>
      <ellipse cx="92" cy="162" rx="34" ry="4" fill="#e8e9eb"/>
      <rect x="0" y="0" width="184" height="125" rx="3" fill="#1b1c20"/>
      <rect x="7" y="7" width="170" height="111" fill="#fff" role="img" aria-label="Screenshot of an application form in the platform"/>
      <rect x="7" y="7" width="35" height="111" fill="#2f3035"/>
      <rect x="48" y="28" width="124" height="10" fill="#eaf5e4"/>
      <g fill="#e6e8ec"><rect x="48" y="50" width="60" height="2"/><rect x="48" y="58" width="30" height="2"/><rect x="48" y="66" width="40" height="2"/><rect x="48" y="76" width="30" height="2"/><rect x="48" y="86" width="50" height="2"/><rect x="48" y="96" width="40" height="2"/></g>
    </svg>
    <div class="abs wordmark inner-wordmark"><span class="dot"></span>Jurnex</div>

    <svg class="abs" style="left:0;top:0" width="853" height="551" viewBox="0 0 853 551" role="img" aria-label="Photo of an award ceremony stage with lights and a large audience">
      <defs><linearGradient id="stage" x1="0" y1="0" x2="1" y2="1"><stop offset="0" stop-color="#1d2c6b"/><stop offset=".55" stop-color="#0e1638"/><stop offset="1" stop-color="#070a1c"/></linearGradient></defs>
      <path d="M432 541C470 420 600 340 853 320V541Z" fill="url(#stage)"/>
    </svg>
    <div class="abs bottom-bar"></div>
  </section>
</div>
</body>
</html>
```